Camp Thornbrook 2021 Magazine Design

We are for someone to design our annual magazine/newsletter. This is a print newsletter that is a total of 20 pages. It will need to be designed in a way that is easy to share with our printers. The designer will need to be someone who is creative and easy to work with.
For those interested in this project we ask that you design 4 to 6 pages for us to view. Once we select the designer we will want the rest created in a two-week time span. For those submitting a bid please include front cover, theme & dates, mission & vision, and Lend a Hand Forward.

This link will provide the layout of the newsletter https://files.pelmarsh.example/doc/7qTzR2kLpW9xVbN4cHsYd/view.

This link will provide you with the pictures that are needed and a few documents https://files.pelmarsh.example/folder/3hGvK8mQxZ5rLtP1wNcBj/view

Details:
20 pages long (including covers)
8.5 x 11

Please message me if you need any further details.

Target Market(s)

Our alumni base. Covers all ages

Requirements
Must have
• Spelled out in document
Nice to have
• Spelled out in document
Should not have
• Spelled out in document

```html
<!DOCTYPE html>
<html lang="en">
<head>
<meta charset="utf-8">
<title>Camp Thornbrook 2021 – Session and Dates</title>
<link rel="stylesheet" href="https://fonts.googleapis.com/css2?family=Graduate&family=Noto+Sans:wght@400&family=Noto+Serif:wght@700&display=swap">
<style>
  :root {
    --orange: #f39c12;
    --forest: #355a28;
    --lime: #dde384;
    --mist: #e9eaea;
    --ink: #2a2a2a;
    --leaf-text: #3b5a26;
    --rule: #333333;
    --white: #ffffff;
    --title-edge: #6b4300;
    --art-hike: #b4c98a;
    --art-ball: #f3b877;
    --art-target: #d9dde6;
    --art-swim: #b3def2;
  }
  * { box-sizing: border-box; margin: 0; padding: 0; }
  html, body { width: 927px; height: 1200px; overflow: hidden; background: var(--white); }
  .page {
    position: relative; width: 927px; height: 1200px;
    border: 1px solid #9a9a9a; overflow: hidden;
    font-family: "Noto Sans", sans-serif; color: var(--ink);
  }
  .top-band { position: absolute; left: 0; top: 0; width: 100%; height: 23px; background: var(--orange); }
  .title-band {
    position: absolute; left: 0; top: 23px; width: 100%; height: 72px; background: var(--forest);
    display: flex; align-items: center; justify-content: center;
  }
  .title-notch { position: absolute; left: 143px; top: 94px; }
  .page-title {
    font-family: "Graduate", serif; font-weight: 400; font-size: 34px; letter-spacing: 2px;
    color: var(--orange); font-variant: small-caps; padding-top: 4px;
    -webkit-text-stroke: 2px var(--title-edge); paint-order: stroke fill;
  }
  table { position: absolute; border-collapse: collapse; table-layout: fixed; }
  td { border: 1px solid var(--rule); font-size: 20px; line-height: 1; }
  .sessions { left: 152px; top: 152px; width: 623px; }
  .sessions td { height: 35.4px; }
  .sessions .name { width: 206px; padding-left: 28px; }
  .sessions .dates { width: 269px; text-align: center; white-space: pre; }
  .sessions .price { width: 148px; text-align: center; }
  .sessions .main .name { background: var(--orange); }
  .sessions .main .dates { background: var(--lime); }
  .sessions .main .price { background: var(--mist); }
  .groups { left: 148px; top: 552px; width: 626px; }
  .groups td { height: 31.5px; text-align: center; }
  .groups .label { width: 90px; text-align: left; padding-left: 14px; }
  .groups .row-group .label { background: var(--orange); }
  .groups .row-group td:not(.label) { background: var(--mist); }
  .groups .row-age .label { background: var(--lime); }
  .activities { position: absolute; left: 140px; top: 678px; list-style: none; color: var(--leaf-text); font-size: 19.5px; }
  .activities li { height: 29px; display: flex; align-items: center; }
  .activities .bullet {
    width: 9px; height: 9px; border: 1.5px solid var(--orange); margin: 0 17px 0 2px; position: relative;
  }
  .activities .bullet::after { content: ""; position: absolute; left: 1.5px; top: 1.5px; width: 3px; height: 3px; background: var(--orange); }
  .art { position: absolute; border-radius: 10px; }
  .art-hike { left: 581px; top: 691px; width: 161px; height: 114px; background: var(--art-hike); }
  .art-ball { left: 500px; top: 818px; width: 137px; height: 124px; background: var(--art-ball); }
  .art-target { left: 695px; top: 821px; width: 137px; height: 107px; background: var(--art-target); }
  .art-swim { left: 527px; top: 956px; width: 289px; height: 110px; background: var(--art-swim); }
  .footer-rule { position: absolute; left: 59px; top: 1144px; width: 815px; height: 2px; background: var(--forest); }
  .page-number {
    position: absolute; left: 59px; top: 1145px; width: 27px; height: 26px; background: var(--forest);
    color: var(--orange); font-family: "Noto Serif", serif; font-weight: 700; font-size: 16px;
    display: flex; align-items: center; justify-content: center;
  }
  .edition-year {
    position: absolute; right: 53px; top: 1146px; font-family: "Noto Serif", serif; font-weight: 700;
    font-size: 21px; letter-spacing: 4px; color: var(--forest);
  }
</style>
</head>
<body>
<div class="page">
  <div class="top-band"></div>
  <header class="title-band"><h1 class="page-title">Session and Dates</h1></header>
  <svg class="title-notch" width="28" height="11" viewBox="0 0 28 11"><polygon points="0,0 28,0 14,11" fill="#355a28"/></svg>

  <table class="sessions">
    <tr class="main"><td class="name">Session 1</td><td class="dates">May  30 - June   5</td><td class="price">($285)</td></tr>
    <tr><td class="name">Short Session 1</td><td class="dates">May  30 - June   2</td><td class="price">($175)</td></tr>
    <tr class="main"><td class="name">Session 2</td><td class="dates">June   6 - June 17</td><td class="price">($425)</td></tr>
    <tr><td class="name">Session 2B</td><td class="dates">June   6 - June 12</td><td class="price">($285)</td></tr>
    <tr class="main"><td class="name">Session 3</td><td class="dates">June 27 - July    8</td><td class="price">($425)</td></tr>
    <tr><td class="name">Session 3B</td><td class="dates">June 27 - July    3</td><td class="price">($285)</td></tr>
    <tr class="main"><td class="name">Session 4</td><td class="dates">July  11 - July  22</td><td class="price">($425)</td></tr>
    <tr><td class="name">Session 4B</td><td class="dates">July  11 - July  17</td><td class="price">($285)</td></tr>
    <tr class="main"><td class="name">Session 5</td><td class="dates">July  25 - July  31</td><td class="price">($285)</td></tr>
    <tr><td class="name">Short Session 2</td><td class="dates">July  25 - July  28</td><td class="price">($175)</td></tr>
  </table>

  <table class="groups">
    <tr class="row-group"><td class="label">Group</td><td>1</td><td>2</td><td>3</td><td>4</td></tr>
    <tr class="row-age"><td class="label">Age</td><td>8-10 Years</td><td>11-12 Years</td><td>13-14 Years</td><td>15-18 Years</td></tr>
  </table>

  <ul class="activities">
    <li><span class="bullet"></span>Archery Tag</li>
    <li><span class="bullet"></span>Blob</li>
    <li><span class="bullet"></span>Horseback Riding</li>
    <li><span class="bullet"></span>Hiking</li>
    <li><span class="bullet"></span>Gaga Ball</li>
    <li><span class="bullet"></span>Golden Goal (New)</li>
    <li><span class="bullet"></span>Rappelling</li>
    <li><span class="bullet"></span>Archery</li>
    <li><span class="bullet"></span>Hatchet Throwing (New)</li>
    <li><span class="bullet"></span>Basketball</li>
    <li><span class="bullet"></span>Arts and Crafts</li>
    <li><span class="bullet"></span>9 Square in the Air</li>
    <li><span class="bullet"></span>Swimming</li>
    <li class="more">And much more!</li>
  </ul>

  <div class="art art-hike" role="img" aria-label="Illustration of campers hiking up a sunny green hill"></div>
  <div class="art art-ball" role="img" aria-label="Illustration of a basketball dropping through a hoop"></div>
  <div class="art art-target" role="img" aria-label="Illustration of an arrow hitting an archery target"></div>
  <div class="art art-swim" role="img" aria-label="Illustration of a child swimming in splashing water"></div>

  <div class="footer-rule"></div>
  <div class="page-number">7</div>
  <div class="edition-year">2021</div>
</div>
</body>
</html>
```